Carton Box Packaging For Motorcycle Brake Shoe - Varonel Brand

Packaging Dimensions: 125mm (H) x 125mm (W) x 31mm (D)
We would like to design a genuine Carton box Packaging for motorcycle Brake Shoe.
This is a critical part of the motorcycle, so we need the packaging to reflect elegant impression.
Varonel, is one of the leading companies for manufacturing Motorcycles, located in Egypt. Our company is offering high-quality products, the best in the local market, with very competitive prices.
We have a limited time to get this project done, So we Highly appreciate receiving your designs ASAP.
Target Market(s)
Economical Motorcycle Buyers
Colors
Designer to choose colors to be used in the design.
Look and feel

```html
<!DOCTYPE html>
<html lang="en">
<head>
<meta charset="utf-8">
<title>Varonel Motorcycle Brake Shoe – Carton Front and Side Panel</title>
<link rel="stylesheet" href="https://fonts.googleapis.com/css2?family=Orbitron:wght@800;900&family=Roboto+Condensed:wght@700&display=swap">
<style>
  :root {
    --carton-red: #e8212b;
    --carton-blue: #0a52a3;
    --carton-yellow: #f7ec1f;
    --ink-white: #ffffff;
    --ink-black: #111111;
    --steel-light: #d9d6cf;
    --steel-dark: #7d7a73;
    --page: #ffffff;
  }
  * { box-sizing: border-box; margin: 0; padding: 0; }
  html, body {
    width: 1200px; height: 1000px; overflow: hidden;
    background: var(--page);
  }
  .dieline {
    position: absolute; left: 200px; top: 180px;
    width: 800px; height: 640px; display: flex;
  }
  .front-panel {
    position: relative; width: 640px; height: 640px; overflow: hidden;
    background: var(--carton-red);
  }
  .front-panel .graphic-rays { position: absolute; inset: 0; }
  .brand-lockup {
    position: absolute; top: 42px; left: 0; width: 100%;
    display: flex; flex-direction: column; align-items: center; gap: 14px;
  }
  .brand-dot {
    width: 120px; height: 120px; border-radius: 50%;
    background: var(--ink-white);
  }
  .brand-name {
    font-family: "Orbitron", sans-serif; font-weight: 900;
    font-size: 30px; letter-spacing: 3px; color: var(--ink-white);
  }
  .product-title {
    position: absolute; top: 218px; left: 0; width: 100%;
    text-align: center; font-family: "Orbitron", sans-serif; font-weight: 900;
    font-size: 42px; line-height: 1.02; color: var(--ink-white);
    -webkit-text-stroke: 2px var(--ink-black); paint-order: stroke fill;
    text-shadow: 3px 3px 0 var(--ink-black);
  }
  .product-visual {
    position: absolute; left: 150px; top: 330px; width: 370px; height: 190px;
    border-radius: 0 0 185px 185px / 0 0 170px 170px;
    background: linear-gradient(180deg, var(--steel-light), var(--steel-dark));
  }
  .quality-badge {
    position: absolute; right: 36px; top: 400px; width: 150px;
    text-align: center; font-family: "Roboto Condensed", sans-serif; font-weight: 700;
    font-size: 27px; line-height: 1.15; color: var(--ink-white);
  }
  .base-band {
    position: absolute; left: 0; bottom: 0; width: 100%; height: 120px;
    background: var(--carton-blue); border-top: 3px solid rgba(0,0,0,.15);
    display: flex; align-items: center; justify-content: center;
  }
  .base-band .brand-name { font-size: 46px; letter-spacing: 6px; }
  .side-panel {
    position: relative; width: 160px; height: 640px;
    background: var(--carton-blue); border-left: 3px solid rgba(255,255,255,.35);
    display: flex; flex-direction: column; align-items: center; justify-content: center; gap: 40px;
  }
  .side-title {
    writing-mode: vertical-rl; transform: rotate(180deg);
    font-family: "Orbitron", sans-serif; font-weight: 900; font-size: 30px; line-height: 1.1;
    text-align: center; color: var(--ink-white);
  }
  .side-brand { display: flex; flex-direction: column; align-items: center; gap: 8px; }
  .side-brand .brand-dot { width: 50px; height: 50px; }
  .side-brand .brand-name { font-size: 14px; letter-spacing: 1px; }
</style>
</head>
<body>
  <main class="dieline">
    <section class="front-panel">
      <svg class="graphic-rays" viewBox="0 0 640 640" width="640" height="640" aria-hidden="true">
        <polygon points="640,165 0,290 0,520" fill="var(--carton-yellow)"/>
        <polygon points="640,168 0,360 0,380" fill="var(--carton-red)"/>
        <polygon points="640,172 0,430 0,455" fill="var(--carton-red)"/>
        <polygon points="640,175 640,640 0,640 0,520" fill="var(--carton-blue)"/>
      </svg>
      <div class="brand-lockup">
        <span class="brand-dot"></span>
        <span class="brand-name">VARONEL</span>
      </div>
      <h1 class="product-title">MOTORCYCLE<br>BRAKE SHOE</h1>
      <div class="product-visual" role="img" aria-label="Product photo of a pair of motorcycle brake shoes with springs"></div>
      <p class="quality-badge">HIGH<br>QUALITY</p>
      <div class="base-band"><span class="brand-name">VARONEL</span></div>
    </section>
    <aside class="side-panel">
      <h2 class="side-title">MOTORCYCLE<br>BRAKE SHOE</h2>
      <div class="side-brand">
        <span class="brand-dot"></span>
        <span class="brand-name">VARONEL</span>
      </div>
    </aside>
  </main>
</body>
</html>
```